Animal Eye Clinic needs a Business card

We are a new veterinary ophthalmology practice (Silverbrook Pet Vision Care) and we need a business card designed. We only see animal eyes - we are not a regular veterinary clinic. We already have a logo. We are looking for a professional, good looking business card to hand out to our clients. We are looking for something simple but professional and contemporary. Our logo is likely the only picture/graphic that needs to be on the card.

Contact Information for Business Card

Marisol Quent, BSc, DVM, MSc, DipACVO
Veterinary Ophthalmologist

Phone: 250.419.3067
Email: silverbrookpetvisioncare@mailvero.com
Website: silverbrookpetvisioncare.com
Address: 1875 Tessock Rd
Kelowna, BC, V4T 8M3

Colors

Designer to choose colors to be used in the design.

Requirements
Must have
• Our logo (attached)

```html
<!DOCTYPE html>
<html lang="en">
<head>
<meta charset="utf-8">
<title>Silverbrook Pet Vision Care – Business Card</title>
<link rel="stylesheet" href="https://fonts.googleapis.com/css2?family=Montserrat:wght@400;500;600;700&display=swap">
<style>
  :root {
    --teal: #1b9aaa;
    --teal-dark: #137f8d;
    --grey: #6b6b6b;
    --grey-mid: #7a7a7a;
    --text-grey: #5a5a5a;
    --white: #ffffff;
    --stage: #e9ecee;
  }
  * { box-sizing: border-box; margin: 0; padding: 0; }
  html, body { width: 1200px; height: 800px; overflow: hidden; }
  body {
    background: var(--stage);
    font-family: "Montserrat", Arial, sans-serif;
    position: relative;
  }
  .card {
    position: absolute;
    width: 540px;
    height: 309px;
    border-radius: 22px;
    overflow: hidden;
    box-shadow: 0 10px 30px rgba(0,0,0,0.18);
  }
  /* Back of card */
  .card-back {
    left: 50px; top: 70px;
    background: linear-gradient(160deg, var(--teal) 0%, var(--grey-mid) 38%, var(--grey) 62%, var(--teal) 100%);
    color: var(--white);
  }
  .card-back .brand {
    position: absolute;
    left: 50px; top: 118px;
    display: flex; align-items: center; gap: 16px;
  }
  .brand-dot {
    width: 52px; height: 52px; border-radius: 50%;
    flex: none;
  }
  .card-back .brand-dot { background: var(--white); }
  .brand-name {
    font-weight: 600;
    font-size: 25px;
    letter-spacing: 0.5px;
    line-height: 1.1;
  }
  .card-back .website {
    position: absolute;
    left: 0; right: 0; bottom: 48px;
    text-align: center;
    font-size: 12px;
    letter-spacing: 0.3px;
  }
  /* Front of card */
  .card-front {
    left: 610px; top: 420px;
    background: var(--white);
    border-bottom: 8px solid var(--teal);
    color: var(--text-grey);
  }
  .card-front .brand {
    position: absolute;
    left: 36px; top: 40px;
    display: flex; align-items: center; gap: 14px;
    color: var(--teal);
  }
  .card-front .brand-dot { background: var(--teal); }
  .card-front .brand-name { font-size: 23px; }
  .person {
    position: absolute;
    left: 36px; top: 124px;
  }
  .person-name {
    font-weight: 700;
    font-size: 14px;
    color: var(--text-grey);
    letter-spacing: 0.2px;
  }
  .person-title {
    font-weight: 500;
    font-size: 14px;
    color: var(--teal);
    margin-top: 4px;
  }
  .details {
    position: absolute;
    left: 36px; right: 30px; bottom: 34px;
    display: flex; align-items: stretch; gap: 14px;
    font-size: 11.5px;
    color: var(--text-grey);
  }
  .contact-list { list-style: none; display: flex; flex-direction: column; gap: 5px; }
  .contact-list li { display: flex; align-items: center; gap: 7px; }
  .contact-list svg { width: 12px; height: 12px; flex: none; fill: var(--teal); }
  .divider { width: 1px; background: var(--teal); }
  .address { display: flex; flex-direction: column; justify-content: center; gap: 5px; }
</style>
</head>
<body>
  <section class="card card-back" aria-label="Business card back">
    <div class="brand">
      <span class="brand-dot"></span>
      <span class="brand-name">Silverbrook Pet<br>Vision Care</span>
    </div>
    <p class="website">www.silverbrookpetvisioncare.com</p>
  </section>

  <section class="card card-front" aria-label="Business card front">
    <div class="brand">
      <span class="brand-dot"></span>
      <span class="brand-name">Silverbrook Pet Vision Care</span>
    </div>
    <div class="person">
      <p class="person-name">MARISOL QUENT, BSC, DVM, MSC, DIPACVO</p>
      <p class="person-title">Veterinary Ophthalmologist</p>
    </div>
    <div class="details">
      <ul class="contact-list">
        <li>
          <svg viewBox="0 0 24 24" aria-hidden="true"><path d="M6.6 10.8a15.1 15.1 0 0 0 6.6 6.6l2.2-2.2a1 1 0 0 1 1-.25 11.4 11.4 0 0 0 3.6.57 1 1 0 0 1 1 1V20a1 1 0 0 1-1 1A17 17 0 0 1 3 4a1 1 0 0 1 1-1h3.5a1 1 0 0 1 1 1c0 1.25.2 2.45.57 3.57a1 1 0 0 1-.25 1z"/></svg>
          250.419.3067
        </li>
        <li>
          <svg viewBox="0 0 24 24" aria-hidden="true"><path d="M3 5h18a1 1 0 0 1 1 1v12a1 1 0 0 1-1 1H3a1 1 0 0 1-1-1V6a1 1 0 0 1 1-1zm9 7.2L4 7.5V8l8 5 8-5v-.5z"/></svg>
          silverbrookpetvisioncare@mailvero.com
        </li>
        <li>
          <svg viewBox="0 0 24 24" aria-hidden="true"><path d="M12 2a10 10 0 1 0 0 20 10 10 0 0 0 0-20zm6.9 6h-2.9a15.7 15.7 0 0 0-1.4-3.6A8 8 0 0 1 18.9 8zM12 4a14 14 0 0 1 1.9 4h-3.8A14 14 0 0 1 12 4zM4.3 14a8 8 0 0 1 0-4h3.4a16.5 16.5 0 0 0 0 4zm.8 2h2.9a15.7 15.7 0 0 0 1.4 3.6A8 8 0 0 1 5.1 16zM8 8H5.1a8 8 0 0 1 4.3-3.6A15.7 15.7 0 0 0 8 8zm4 12a14 14 0 0 1-1.9-4h3.8A14 14 0 0 1 12 20zm2.3-6H9.7a14.7 14.7 0 0 1 0-4h4.6a14.7 14.7 0 0 1 0 4zm.3 5.6A15.7 15.7 0 0 0 16 16h2.9a8 8 0 0 1-4.3 3.6zM16.3 14a16.5 16.5 0 0 0 0-4h3.4a8 8 0 0 1 0 4z"/></svg>
          silverbrookpetvisioncare.com
        </li>
      </ul>
      <span class="divider"></span>
      <address class="address" style="font-style:normal">
        <span>1875 Tessock Rd</span>
        <span>Kelowna, BC, V4T 8M3</span>
      </address>
    </div>
  </section>
</body>
</html>
```